Tuition Center Website

We need a new web site for a tutoring company based in sydney.

We only teach senior highschool students and pride ourselves on building the students abilities to think their way through life.

I would like a bright and vibrant website that looks professional and modern.
It needs to look simple and neat but also have the functionality we need.
Images and flash would be good.

Please keep in mind that the site must be appealing to a younger audience.

We need a multipage website with the following navigation bars:

1.Home (As logo not "home" button)
I would like a news box/ticker somewhere that can stream our chatterbook and flitter feeds and also any news updates we want to put up.
Subscribe to newsletter button.

2. About us.
This needs to be a pull down into:
-What we do
-Why we do it
-How we do it

3. Courses
Pulldown into:
-Maths
-English
-Science
(we may need to attach extra pages behind these e.g. Courses/Science/Physics or Courses/Science/Chemistry and possibly add a link to a new quizzo form)

4. Inspired
This page is like a blog page where we can upload videos, links to articles that we find to be inspiring and hopefully will inspire others.

5. Inspire
This is a recruitment page. Only content here.

6. Contact us.
Mapzy map widget and a 'contact us' form

* Our branding requires green close to #12FF3D

***Please have a look at the current website.
@ www.brindlelearning.com.au

Thanks everybody hope the revision of my brief is better and more informative than my last one

Target Market(s)

senior highschool students aged 15-19, parents ( to a lesser degree)

Industry/Entity Type

It Company

Requirements
Must have
• Ability to change content on pages.

The green doesn't have to be everywhere, but it must be obvious that it is our colour.

Nice to have
• Sites with a nicer mix of images and flash will be given more consideration. But then again, if you amaze us, you amaze us and we will go with your design.
Should not have
• Should stay away from ocre, brown colours and serif fonts.

```html
<!DOCTYPE html>
<html lang="en">
<head>
<meta charset="utf-8">
<title>Brindle Learning – HSC coaching &amp; mentoring</title>
<link href="https://fonts.googleapis.com/css2?family=Open+Sans:ital,wght@0,400;0,600;0,700;1,700&display=swap" rel="stylesheet">
<style>
:root{
  --green:#7ab51d;
  --green-bright:#6fd400;
  --btn-top:#6cb52a;
  --btn-bottom:#3f8a12;
  --ink:#111;
  --text:#333;
  --rule:#d6d6d6;
  --footer:#000;
  --white:#fff;
}
*{margin:0;padding:0;box-sizing:border-box}
html,body{width:1146px;height:1200px;overflow:hidden;background:var(--white)}
body{position:relative;font-family:"Open Sans",Arial,sans-serif;color:var(--text)}
.abs{position:absolute}

/* header */
.site-header{left:0;top:0;width:1146px;height:94px;background:linear-gradient(#fff,#ececec);border-bottom:1px solid #cfcfcf;box-shadow:0 2px 4px rgba(0,0,0,.15);z-index:3}
.brand{left:116px;top:30px;display:flex;align-items:center;gap:8px}
.brand-mark{width:26px;height:26px;background:var(--green-bright)}
.brand-name{font-size:18px;font-weight:600;color:var(--green)}
.main-nav{right:65px;top:44px;display:flex;font-size:14px;color:#222}
.main-nav span{padding:0 14px}
.main-nav .sep{padding:0}

/* hero */
.hero{left:0;top:94px;width:1146px;height:475px;background:linear-gradient(100deg,#d9d2c8 0%,#f1f1ef 35%,#f5f5f3 55%,#c9d3dc 78%,#27508f 100%)}
.hero-panel{left:115px;top:193px;width:471px;height:239px;background:rgba(40,40,40,.78);color:var(--white);padding:14px 26px}
.hero-title{font-size:35px;font-weight:400;line-height:1.2}
.hero-sub{font-size:28px;font-weight:400;line-height:1.3}
.hero-copy{font-size:13.4px;line-height:19px;margin-top:12px}
.btn{display:inline-block;background:linear-gradient(var(--btn-top),var(--btn-bottom));color:var(--white);font-weight:600;border-radius:2px}
.hero-panel .btn{font-size:16px;padding:6px 7px;margin-top:11px}

/* welcome */
.welcome{left:135px;top:596px;width:582px;height:258px;border-top:1px solid var(--rule);border-bottom:1px solid var(--rule)}
.welcome h2{position:absolute;left:1px;top:18px;font-size:22px;font-weight:400;color:var(--ink)}
.welcome p{position:absolute;left:0;width:390px;font-size:11px;line-height:17px;color:#222}
.welcome .btn{position:absolute;left:0;top:211px;font-size:15px;font-weight:400;padding:5px 11px}
.welcome-photo{left:540px;top:597px;width:177px;height:256px;background:linear-gradient(#f4f0ec,#d8c6b3)}

/* trial box */
.trial{left:735px;top:605px;width:296px;height:239px;border:1px solid #ccc;background:repeating-linear-gradient(#fff 0 3px,#eef6e2 3px 4px) top/100% 75px no-repeat,linear-gradient(#fff,#f4f4f4);box-shadow:2px 3px 0 #bbb}
.trial h3{position:absolute;left:19px;top:14px;font-size:24px;line-height:25px;font-weight:700;color:var(--ink)}
.trial h3 .big{font-size:30px}
.trial-mark{left:20px;top:87px;width:49px;height:51px;background:var(--green-bright)}
.trial p{position:absolute;left:82px;top:85px;width:210px;font-size:14.3px;line-height:20px;color:#111}
.trial .btn{position:absolute;left:79px;top:178px;font-size:16px;padding:6px 12px;border-radius:0}

/* statement */
.statement{left:135px;top:876px;width:575px;font-size:20px;line-height:26px;color:#111}
.statement b{color:var(--green);font-weight:700}
.statement em{font-weight:700;font-style:italic}

.belief{top:986px;width:260px}
.belief h4{font-size:25px;font-weight:400;color:var(--green);margin-bottom:8px}
.belief li{list-style:none;font-size:15px;line-height:25px;color:#333;padding-left:30px;position:relative}
.belief li svg{position:absolute;left:0;top:5px}

/* news */
.news{left:736px;top:874px;width:295px}
.news h4{font-size:22px;font-weight:400;color:var(--ink);padding-bottom:8px;border-bottom:3px double var(--rule)}
.news li{list-style:none;font-size:12.8px;height:36px;line-height:36px;border-bottom:1px solid var(--rule);padding-left:20px;position:relative;color:#333}
.news li svg{position:absolute;left:0;top:14px}

/* footer */
.site-footer{left:0;top:1145px;width:1146px;height:55px;background:var(--footer);color:var(--white);font-size:11.5px}
.foot-nav{left:135px;top:21px;display:flex;gap:21px}
.copyright{right:115px;top:21px}
.copyright b{color:var(--green);font-weight:400}
</style>
</head>
<body>

<header class="abs site-header">
  <div class="abs brand"><span class="brand-mark"></span><span class="brand-name">Brindle Learning</span></div>
  <nav class="abs main-nav">
    <span>Home</span><span class="sep">|</span><span>About Us</span><span class="sep">|</span><span>Courses</span><span class="sep">|</span><span>Inspired</span><span class="sep">|</span><span>Contact Us</span>
  </nav>
</header>

<section class="abs hero" role="img" aria-label="Photo of a smiling teacher writing maths on a whiteboard in front of students"></section>
<div class="abs hero-panel">
  <h1 class="hero-title">I Am Brindle</h1>
  <div class="hero-sub">real HSC coaching &amp; mentoring</div>
  <p class="hero-copy">The HSC help you need, in the years you need it. We offer small classes, individualised attention and genuine care for each student. It's different - in a good way. Feel free to find out more about us, and let us know if there's any way we can help you on your journey.</p>
  <span class="btn">Enquire Now</span>
</div>

<section class="abs welcome">
  <h2>Welcome to Brindle</h2>
  <p style="top:64px">Lorem Ipsum is simply dummy text of the printing and typesetting industry. Lorem Ipsum has been the industry's standard dummy text ever since the 1500s,</p>
  <p style="top:154px">when an unknown printer took a galley of type and scrambled it to make a type specimen book. It has survived not only five centuries, but also the leap into electronic typesetting, remaining essentially unchanged.</p>
  <span class="btn">Read More</span>
</section>
<div class="abs welcome-photo" role="img" aria-label="Photo of a smiling schoolgirl holding a blue folder and a marker"></div>

<aside class="abs trial">
  <h3>Ask For Your<br><span class="big">Free Trial Lesson</span></h3>
  <div class="abs trial-mark"></div>
  <p>Because we believe you shouldn't have to sign up until you see what it's actually like. Call or email us now!</p>
  <span class="btn">Send an Enquiry</span>
</aside>

<p class="abs statement">Brindle Learning are <b>HSC</b> mentors and tutors who aim to <em>build real relationships</em> and offer you the help you need. <b>HSC</b> tutoring is different at Brindle – in a good way.</p>

<div class="abs belief" style="left:135px">
  <h4>We Don’t Believe In:</h4>
  <ul>
    <li><svg width="20" height="15" viewBox="0 0 20 15"><path d="M2 5v9h14v-4" fill="none" stroke="#7ab51d" stroke-width="2.5"/><path d="M6 10c1-4 5-6 9-6V1l5 5-5 5V8c-4 0-7 1-9 2z" fill="#7ab51d"/></svg>Massive classes;</li>
    <li><svg width="20" height="15" viewBox="0 0 20 15"><path d="M2 5v9h14v-4" fill="none" stroke="#7ab51d" stroke-width="2.5"/><path d="M6 10c1-4 5-6 9-6V1l5 5-5 5V8c-4 0-7 1-9 2z" fill="#7ab51d"/></svg>Spoon-feeding answers;</li>
    <li><svg width="20" height="15" viewBox="0 0 20 15"><path d="M2 5v9h14v-4" fill="none" stroke="#7ab51d" stroke-width="2.5"/><path d="M6 10c1-4 5-6 9-6V1l5 5-5 5V8c-4 0-7 1-9 2z" fill="#7ab51d"/></svg>One-size-fits-all teaching.</li>
  </ul>
</div>
<div class="abs belief" style="left:452px">
  <h4>We Don’t Believe In:</h4>
  <ul>
    <li><svg width="20" height="15" viewBox="0 0 20 15"><path d="M2 5v9h14v-4" fill="none" stroke="#7ab51d" stroke-width="2.5"/><path d="M6 10c1-4 5-6 9-6V1l5 5-5 5V8c-4 0-7 1-9 2z" fill="#7ab51d"/></svg>Small classes tailored to you;</li>
    <li><svg width="20" height="15" viewBox="0 0 20 15"><path d="M2 5v9h14v-4" fill="none" stroke="#7ab51d" stroke-width="2.5"/><path d="M6 10c1-4 5-6 9-6V1l5 5-5 5V8c-4 0-7 1-9 2z" fill="#7ab51d"/></svg>Helping you think for yourself;</li>
    <li><svg width="20" height="15" viewBox="0 0 20 15"><path d="M2 5v9h14v-4" fill="none" stroke="#7ab51d" stroke-width="2.5"/><path d="M6 10c1-4 5-6 9-6V1l5 5-5 5V8c-4 0-7 1-9 2z" fill="#7ab51d"/></svg>Genuinely caring about who you are as an individual.</li>
  </ul>
</div>

<section class="abs news">
  <h4>Recent News</h4>
  <ul>
    <li><svg width="11" height="9" viewBox="0 0 11 9"><path d="M1 4.5l3 3 6-6" fill="none" stroke="#7ab51d" stroke-width="2"/></svg>Year 11 FREE HSC Workshops!</li>
    <li><svg width="11" height="9" viewBox="0 0 11 9"><path d="M1 4.5l3 3 6-6" fill="none" stroke="#7ab51d" stroke-width="2"/></svg>Uni Open Days 2012</li>
    <li><svg width="11" height="9" viewBox="0 0 11 9"><path d="M1 4.5l3 3 6-6" fill="none" stroke="#7ab51d" stroke-width="2"/></svg>Considering Studying Interstate</li>
    <li><svg width="11" height="9" viewBox="0 0 11 9"><path d="M1 4.5l3 3 6-6" fill="none" stroke="#7ab51d" stroke-width="2"/></svg>Year 11 Free Hsc Workshops!</li>
    <li><svg width="11" height="9" viewBox="0 0 11 9"><path d="M1 4.5l3 3 6-6" fill="none" stroke="#7ab51d" stroke-width="2"/></svg>Uni Open Days 2012</li>
    <li style="border-bottom:none"><svg width="11" height="9" viewBox="0 0 11 9"><path d="M1 4.5l3 3 6-6" fill="none" stroke="#7ab51d" stroke-width="2"/></svg>Considering Studying Interstate</li>
  </ul>
</section>

<footer class="abs site-footer">
  <nav class="abs foot-nav"><span>Home</span><span>About us</span><span>Courses</span><span>Inspired</span><span>Contact Us</span></nav>
  <div class="abs copyright">Copyright © 2013 brindle learning | <b>HSC</b> tutoring &amp; mentoring</div>
</footer>

</body>
</html>
```